Wendale Ridge Concrete Pumping needs a logo design and is in the concrete industry

A creative design for this Wendale Ridge Concrete Pumping business. Using a trailer mounted line pump, not a boom pump.
Colour to be used is orange and a mix of white or black writing.
Target Market(s)
General Public, anyone
Industry/Entity Type
Concrete
Contact Information for Business Card
Wendale Ridge Concrete Pumping
Callum Hesketh
PO BOX 47
Birchmoor VIC 3391
Phone: 0417952803
Email: Hesketh@bluewrenmail.com.au
Colors
f37122
000000
ffffff
Requirements
Must have
- Details listed
Nice to have
- A great logo
Should not have
- anything silly

```html
<!DOCTYPE html>
<html lang="en">
<head>
<meta charset="utf-8">
<title>Wendale Ridge Concrete Pumping – Business Card</title>
<link rel="stylesheet" href="https://fonts.googleapis.com/css2?family=Audiowide&family=Roboto:wght@400&display=swap">
<style>
  :root {
    --orange: #f37122;
    --black: #1c1b1b;
    --card-dark: #141414;
    --white: #ffffff;
    --silver: #d9d9d9;
    --backdrop: #c89d6c;
    --ink: #111111;
  }
  * { margin: 0; padding: 0; box-sizing: border-box; }
  html, body { width: 1181px; height: 1200px; overflow: hidden; }
  body { background: var(--backdrop); position: relative; font-family: "Roboto", sans-serif; }

  .card {
    position: absolute; left: 230px; width: 722px; height: 454px;
    border-radius: 22px; overflow: hidden;
  }
  .card--front { top: 101px; background: var(--white); }
  .card--back { top: 642px; background: var(--card-dark); }

  .brand { position: absolute; display: flex; align-items: center; gap: 14px; }
  .brand__mark { width: 18px; height: 18px; background: var(--orange); flex: none; }
  .brand__name {
    font-family: "Audiowide", sans-serif; font-size: 27px; line-height: 1.15;
    color: var(--ink);
  }
  .card--front .brand { left: 42px; top: 180px; }
  .card--back .brand { left: 170px; top: 188px; }
  .card--back .brand__name { color: var(--silver); font-size: 34px; }
  .card--back .brand__mark { width: 22px; height: 22px; }

  .divider {
    position: absolute; left: 368px; top: 121px; width: 2px; height: 213px;
    background: var(--orange);
  }

  .contact { position: absolute; left: 405px; top: 142px; }
  .contact__name {
    font-family: "Audiowide", sans-serif; font-size: 24px; color: var(--ink);
    line-height: 1.1;
  }
  .contact__role { color: var(--orange); font-size: 19px; margin-top: 2px; }
  .contact__list { list-style: none; margin-top: 10px; }
  .contact__item {
    display: flex; align-items: flex-start; gap: 10px;
    font-size: 18px; color: var(--ink); line-height: 23px; margin-bottom: 8px;
  }
  .contact__icon { width: 14px; height: 16px; flex: none; margin-top: 4px; fill: var(--orange); }

  .band { position: absolute; left: 0; bottom: 0; width: 722px; height: 31px; }
</style>
</head>
<body>
  <section class="card card--front" aria-label="Business card front">
    <div class="brand">
      <span class="brand__mark"></span>
      <span class="brand__name">Wendale Ridge<br>Concrete Pumping</span>
    </div>
    <div class="divider"></div>
    <div class="contact">
      <h1 class="contact__name">Callum Hesketh</h1>
      <p class="contact__role">Job Title</p>
      <ul class="contact__list">
        <li class="contact__item">
          <svg class="contact__icon" viewBox="0 0 14 16" aria-hidden="true"><path d="M7 0a5.5 5.5 0 0 0-5.5 5.5C1.5 9.6 7 16 7 16s5.5-6.4 5.5-10.5A5.5 5.5 0 0 0 7 0zm0 7.8a2.3 2.3 0 1 1 0-4.6 2.3 2.3 0 0 1 0 4.6z"/></svg>
          <span>PO BOX 47<br>Birchmoor VIC 3391</span>
        </li>
        <li class="contact__item">
          <svg class="contact__icon" viewBox="0 0 14 16" aria-hidden="true"><path d="M0 6c0-2 3-3 7-3s7 1 7 3v1.5h-3.5V6h-7v1.5H0zM2.5 8.5l1.5-1.5h6l1.5 1.5V13h-9zM7 9a1.8 1.8 0 1 0 0 3.6A1.8 1.8 0 0 0 7 9z"/></svg>
          <span>0417952803</span>
        </li>
        <li class="contact__item">
          <svg class="contact__icon" viewBox="0 0 14 16" aria-hidden="true"><path d="M0 5h14v1L7 10 0 6zM0 7.3l7 4 7-4V13H0z"/></svg>
          <span>Hesketh@bluewrenmail.com.au</span>
        </li>
      </ul>
    </div>
    <svg class="band" viewBox="0 0 722 31" aria-hidden="true">
      <polygon points="0,0 373,0 392,31 0,31" fill="var(--orange)"/>
      <polygon points="379,0 722,0 722,31 398,31" fill="var(--black)"/>
    </svg>
  </section>

  <section class="card card--back" aria-label="Business card back">
    <div class="brand">
      <span class="brand__mark"></span>
      <span class="brand__name">Wendale Ridge<br>Concrete Pumping</span>
    </div>
  </section>
</body>
</html>
```